Logo and business card

RVK Financial Solutions - Branding & Image Project

There will be 3 companies in our group. We want a similar Branding look & feel for all 3. The first company is DLW Financial which is already established, and I have included samples of the branding.

The goal for this design project is to create the corporate branding for RVK Financial Solutions which is the second company in the group.

Please use the same colours and fonts that we use at DLW Financial but the logo must be different. The final design should communicate financial safety and growth. Our typical clients are 40+ years and financially conservative.

Can you create a sample version using the dark green in the attached image.

We will need print resolution files and low res file for email, web etc.

The main printed outputs we need are – see separate attachment for examples;
Business Card 2 sided
Web logo

We’ll then need the following
Letterhead & follow on sheets
Envelopes C5 2 sided & C4 2 sided
Compliment Slips

```html
<!DOCTYPE html>
<html lang="en">
<head>
<meta charset="utf-8">
<title>RVK Financial Solutions – Business Card</title>
<link rel="stylesheet" href="https://fonts.googleapis.com/css2?family=Open+Sans:wght@300;400;700&display=swap">
<style>
  :root {
    --gold: #c38a40;
    --gold-deep: #b67c33;
    --ink: #1e1e1e;
    --mark-grey: #5a5a5a;
    --paper: #ffffff;
    --backdrop: #cfcfcf;
  }
  * { box-sizing: border-box; margin: 0; padding: 0; }
  html, body {
    width: 1200px; height: 900px; overflow: hidden;
    background: var(--backdrop);
    font-family: "Open Sans", Arial, sans-serif;
  }
  .sheet {
    position: relative; width: 1200px; height: 900px;
    display: flex; align-items: center; justify-content: center; gap: 40px;
  }
  .card {
    position: relative; width: 540px; height: 350px;
    border-radius: 26px; overflow: hidden;
  }
  /* Back side */
  .card--back { background: var(--gold); color: var(--paper); }
  .card--back .wordmark {
    position: absolute; left: 70px; top: 120px;
    display: flex; align-items: center; gap: 16px;
  }
  .wordmark__dot {
    width: 22px; height: 22px; border-radius: 50%;
  }
  .card--back .wordmark__dot { background: var(--paper); }
  .wordmark__name {
    font-weight: 300; font-size: 34px; letter-spacing: 0.5px; line-height: 1;
  }
  .legal {
    position: absolute; left: 40px; right: 40px; bottom: 70px;
    text-align: center; font-size: 11.5px; line-height: 1.45; font-weight: 400;
  }
  /* Front side */
  .card--front { background: var(--paper); color: var(--ink); }
  .card--front .wordmark {
    position: absolute; left: 36px; top: 40px;
    display: flex; align-items: center; gap: 14px;
  }
  .card--front .wordmark__dot { background: var(--gold); }
  .card--front .wordmark__name { color: var(--mark-grey); font-size: 28px; }
  .person { position: absolute; left: 36px; top: 128px; }
  .person__name { color: var(--gold); font-weight: 700; font-size: 27px; line-height: 1.1; }
  .person__title { font-size: 15px; margin-top: 2px; }
  .contacts {
    position: absolute; left: 36px; top: 212px; list-style: none;
    font-size: 14.5px; line-height: 1.55;
  }
  .contacts li { display: flex; align-items: center; gap: 10px; }
  .contacts svg { width: 17px; height: 17px; flex: none; }
  .accent { color: var(--gold); }
  .address {
    position: absolute; right: 34px; top: 128px;
    text-align: right; font-style: normal; font-size: 14px; line-height: 1.5;
  }
</style>
</head>
<body>
<main class="sheet">

  <section class="card card--back" aria-label="Business card, back">
    <div class="wordmark">
      <span class="wordmark__dot"></span>
      <span class="wordmark__name">rvk financial solutions</span>
    </div>
    <p class="legal">
      RVK Financial Solutions Limited is authorised and regulated by the Financial<br>
      Conduct Authority reference 512804.<br>
      Registered in England and Wales No. 609317
    </p>
  </section>

  <section class="card card--front" aria-label="Business card, front">
    <div class="wordmark">
      <span class="wordmark__dot"></span>
      <span class="wordmark__name">rvk financial solutions</span>
    </div>

    <div class="person">
      <h1 class="person__name">Morgan Ellery</h1>
      <p class="person__title">Senior Wealth Adviser</p>
    </div>

    <ul class="contacts">
      <li>
        <svg viewBox="0 0 16 16" aria-hidden="true"><rect width="16" height="16" rx="2" fill="var(--gold)"/><path d="M5 3.5l1.6 2.3-1 1c.6 1.3 1.4 2.1 2.6 2.7l1-1 2.3 1.5-.8 1.8c-3.6-.3-6.5-3.2-6.7-6.8z" fill="#fff"/></svg>
        01632 960418
      </li>
      <li>
        <svg viewBox="0 0 16 16" aria-hidden="true"><rect width="16" height="16" rx="2" fill="var(--gold)"/><rect x="5" y="3" width="6" height="10" rx="1" fill="none" stroke="#fff" stroke-width="1.4"/></svg>
        07700 900374
      </li>
      <li>
        <svg viewBox="0 0 16 16" aria-hidden="true"><rect width="16" height="16" rx="2" fill="var(--gold)"/><rect x="3" y="4.5" width="10" height="7" fill="none" stroke="#fff" stroke-width="1.2"/><path d="M3 4.5l5 4 5-4" fill="none" stroke="#fff" stroke-width="1.2"/></svg>
        morgan.ellery@rvkfs.co.uk
      </li>
      <li>
        <svg viewBox="0 0 16 16" aria-hidden="true"><rect width="16" height="16" rx="2" fill="var(--gold)"/><circle cx="8" cy="8" r="4.6" fill="none" stroke="#fff" stroke-width="1.1"/><ellipse cx="8" cy="8" rx="2" ry="4.6" fill="none" stroke="#fff" stroke-width="1"/><path d="M3.4 8h9.2" stroke="#fff" stroke-width="1"/></svg>
        <span>www.<span class="accent">rvkfs</span>.co.uk</span>
      </li>
    </ul>

    <address class="address">
      The Mill House, Unit 4<br>
      Harrow Lane Business Park<br>
      Kingsley Road, Oakworth<br>
      Ashby, Herts, AB1 2CD
    </address>
  </section>

</main>
</body>
</html>
```